Flyer Design for a Boston Therapeutic Clinic

I am a body therapist who needs a couple of flyers designed:
1. To fit half a page.
2. To fit a 5 inch by 3.5 inch flyer.
My practice is based in Boston, MA and my web site is:
www.LarchTessvik.Com
For the First half page:
A. Have my company's name and color shown as it appears on my web site (Larch Tessvik)
B. Have the following text: "Control your weight (This part should be emphasized) by balancing your nervous and digestive system through the Tessvik Method. The Tessvik Method, a technique developed by Dr. Mara. Tessvik, uses physical pressure to manipulate visceral tissue to bring back resiliency and proper functioning of the whole body."
Also helps with
-Constipation
-Bloating
-IBS
-eating disorders and overeating
Our practitioner is highly experienced. Please visit our web sites for reviews.
C. I would like to have a nice earthy feeling, something that feels "freeing" like open flowers, or an open land scape such as mountains or fields.
D. I also like the color blue, white, orange; perhaps if these colors can be integrated into the flyer, that would be great.
E. "Visit our web site LarchTessvik.com or call 786-555-0148"
The Smaller Flyer :
A.The smaller Flyer should also have my Company's name as shown on my web site (Larch Tessvik)
B.The following text: " Restore your body's natural resiliency and greatly reduce your physical pain through the Dr. Mara Tessvik Method of Structural Integration."
C. "Our practitioner is highly experienced and has a great reputation; visit our web site for reviews."
"Benefits:
"reduce aches and pains
reduce joint pain
reduce chronic muscular tension"
D, "feel better after the first session!"
E. if you could use a picture of me working on someone from my web site, that would be great.
F. I also like the colors white, orange and silver, for this one.
G. "Visit our web site LarchTessvik.com or call 786-555 0148"
I am very open minded,
I would like the flyer to evoke a sense of tranquility, professionalism, and simplicity. So if you have another angle you think would look good, then go for it! As long as it looks clean, professional and helpful.
Thanks a lot!
If you need any pictures from my web site, I have the original high resolution files that i can send.
Professionals and working men and women from ages 20-70
Clinic

```html
<!DOCTYPE html>
<html lang="en">
<head>
<meta charset="utf-8">
<title>Larch Tessvik Therapy Flyer</title>
<link href="https://fonts.googleapis.com/css2?family=Rokkitt:wght@300;400&family=Quicksand:wght@600;700&family=Open+Sans:ital,wght@1,400&display=swap" rel="stylesheet">
<style>
  :root {
    --orange: #ff6a00;
    --sage: #8b9e74;
    --olive: #5e6546;
    --olive-edge: #a7b48f;
    --ink: #2e3127;
    --white: #ffffff;
    --blue: #1f4f8f;
    --skin-light: #c9a078;
    --skin-dark: #7a5236;
  }
  html, body { margin: 0; padding: 0; overflow: hidden; background: #ffffff; }
  .flyer {
    position: relative;
    width: 1200px;
    height: 856px;
    overflow: hidden;
    font-family: "Quicksand", sans-serif;
  }
  .flyer-shapes { position: absolute; inset: 0; }
  .brand {
    position: absolute;
    left: 40px;
    top: 68px;
    margin: 0;
    font-family: "Rokkitt", serif;
    font-weight: 300;
    line-height: 1;
  }
  .brand-first {
    display: block;
    font-size: 58px;
    color: var(--orange);
    text-shadow: 2px 3px 6px rgba(0,0,0,0.45);
    letter-spacing: 1px;
  }
  .brand-second {
    display: block;
    margin-top: 10px;
    font-size: 58px;
    color: var(--ink);
    letter-spacing: 0.5px;
  }
  .pitch {
    position: absolute;
    left: 40px;
    margin: 0;
    color: var(--white);
    font-weight: 700;
    font-size: 25px;
    line-height: 35.5px;
    letter-spacing: 0;
  }
  .pitch-emphasis {
    color: var(--blue);
    font-size: 27px;
  }
  .pitch-lead { top: 226px; }
  .pitch-method { top: 438px; }
  .pitch-tail { left: 308px; top: 580px; }
  .helps {
    position: absolute;
    left: -12px;
    top: 590px;
    width: 296px;
    height: 162px;
    background: var(--olive);
    border: 3px solid var(--olive-edge);
    border-radius: 16px;
    box-sizing: border-box;
    color: var(--white);
    text-align: center;
    padding: 14px 0 0 12px;
  }
  .helps-title { margin: 0; font-weight: 700; font-size: 23px; }
  .helps-list {
    list-style: none;
    margin: 6px 0 0;
    padding: 0;
    font-family: "Open Sans", sans-serif;
    font-style: italic;
    font-size: 17px;
    line-height: 23.5px;
  }
  .reviews {
    position: absolute;
    left: 58px;
    top: 772px;
    margin: 0;
    font-family: "Open Sans", sans-serif;
    font-style: italic;
    font-size: 18px;
    line-height: 25px;
    letter-spacing: 1.6px;
    color: var(--ink);
  }
  .web-tab {
    position: absolute;
    left: 1119px;
    top: 212px;
    width: 100px;
    height: 432px;
    background: var(--orange);
    border-radius: 22px 0 0 22px;
  }
  .web-tab::before {
    content: "";
    position: absolute;
    left: 7px; top: 7px; bottom: 7px; right: 0;
    border: 2px solid var(--white);
    border-right: none;
    border-radius: 17px 0 0 17px;
  }
  .web-address {
    position: absolute;
    left: 1160px;
    top: 428px;
    transform: translate(-50%, -50%) rotate(-90deg);
    color: var(--white);
    font-weight: 600;
    font-size: 29px;
    letter-spacing: 2.5px;
    white-space: nowrap;
  }
  .call-out {
    position: absolute;
    left: 580px;
    top: 786px;
    width: 590px;
    height: 46px;
    margin: 0;
    background: var(--blue);
    border: 2px solid var(--white);
    border-radius: 23px;
    box-sizing: border-box;
    color: var(--white);
    font-weight: 700;
    font-size: 18px;
    line-height: 42px;
    text-align: center;
    white-space: nowrap;
  }
</style>
</head>
<body>
<main class="flyer">
  <svg class="flyer-shapes" width="1200" height="856" viewBox="0 0 1200 856">
    <defs>
      <radialGradient id="skin" cx="0.55" cy="0.45" r="0.7">
        <stop offset="0" stop-color="#c9a078"/>
        <stop offset="1" stop-color="#7a5236"/>
      </radialGradient>
    </defs>
    <rect class="therapy-photo" x="460" y="0" width="740" height="856" fill="url(#skin)" role="img" aria-label="Photo of a therapist's hands pressing on a client's bare back"/>
    <path class="accent-sweep" fill="#ff6a00" d="M0,0 H625 C585,100 500,250 502,400 C504,560 548,720 544,856 H0 Z"/>
    <path class="text-panel" fill="#8b9e74" d="M0,56 H540 C495,150 466,270 468,400 C470,560 508,720 504,856 H0 Z"/>
  </svg>

  <h1 class="brand">
    <span class="brand-first">Larch</span>
    <span class="brand-second">Tessvik Therapy</span>
  </h1>

  <p class="pitch pitch-lead">“<strong class="pitch-emphasis">Control your weight</strong> by<br>balancing your nervous and<br>digestive system through<br>the Tessvik Method, a technique<br>developed by Dr. Mara.</p>
  <p class="pitch pitch-method">The Tessvik Method uses<br>physical pressure to manipu-<br>late visceral tissue to bring<br>back resiliency and proper</p>
  <p class="pitch pitch-tail">function-<br>ing of<br>the whole<br>body.”</p>

  <section class="helps">
    <h2 class="helps-title">Also helps with:</h2>
    <ul class="helps-list">
      <li>Constipation</li>
      <li>Bloating</li>
      <li>IBS</li>
      <li>Eating disorders</li>
    </ul>
  </section>

  <p class="reviews">Our practitioner is highly experienced.<br>Please visit our web sites for reviews.</p>

  <p class="call-out">Visit our web site LarchTessvik.com or call 786-555-0148</p>

  <div class="web-tab"></div>
  <div class="web-address">www.LarchTessvik.com</div>
</main>
</body>
</html>
```